Online homewares store needs a web design

We need a web design for a new high-end online homewares store. We are starting small with only 5 major categories.

Rugs
Bathe
Dine
Decorative
Sleep

This is just for design. No coding needed.

Please make high-end, sophisticated and minimal.

I have included some pictures to give you an idea of the products. I would like to showcase some of the pictures on the web page.

The website will be using an e-commerce function.

I have included the logo parlour nine hopes.

I like this website
http://marblewindowhouse.example/

or

brinqlotvane.example.au

Simple but effective - not too busy
Updates

Project Deadline Extended
Reason: I would like to extend my deadline to give designers more time to do quality work - as requested!! Thanks.

Target Market(s)

Females in the age bracket of 25-45

Males who are very house proud 25-45

Industry/Entity Type

Store

Requirements
Must have
• Upmarket

```html
<!DOCTYPE html>
<html lang="en">
<head>
<meta charset="utf-8">
<title>Parlour Nine Hopes – Homewares</title>
<link href="https://fonts.googleapis.com/css2?family=Open+Sans:ital,wght@0,300;0,400;0,600;1,400&family=Jost:wght@400;500&family=Didact+Gothic&display=swap" rel="stylesheet">
<style>
  :root{
    --ink:#000000;
    --footer:#111111;
    --pink:#e8105e;
    --pink-soft:#e2427f;
    --white:#ffffff;
    --grey-band:#d9d9d9;
    --card:#ededed;
    --card-edge:#dddddd;
    --label-bg:rgba(40,40,40,.72);
    --field:#3a3a3a;
    --field-edge:#555555;
  }
  *{box-sizing:border-box;margin:0;padding:0}
  html,body{width:832px;height:1200px;overflow:hidden;background:var(--white)}
  body{position:relative;font-family:"Open Sans",Arial,sans-serif;color:var(--white)}
  .abs{position:absolute}

  /* header */
  .site-header{left:0;top:0;width:832px;height:94px;background:var(--ink)}
  .utility{top:6px;font-size:9px;color:var(--white)}
  .utility.cart{left:622px}
  .utility.items{left:687px}
  .brand{left:99px;top:20px;font-weight:300;font-size:30px;letter-spacing:-.3px;color:var(--white)}
  .main-nav{left:94px;top:69px;display:flex;font-size:11.5px}
  .main-nav a{color:var(--white);text-decoration:none;height:21px;line-height:20px;padding:0 10px}
  .main-nav a.current{border:1px solid var(--pink);margin-right:6px}
  .main-nav a+a{margin-left:8px}
  .social{left:644px;top:65px;display:flex;gap:3px}
  .social span{width:21px;height:21px;border:1px solid var(--pink);border-radius:50%;display:flex;align-items:center;justify-content:center}

  /* hero */
  .hero-band{left:0;top:94px;width:832px;height:283px;background:linear-gradient(90deg,#c9c9c9,#e8e8e8 15%,#e8e8e8 85%,#c9c9c9)}
  .hero-left{left:94px;top:105px;width:298px;height:272px;background:linear-gradient(160deg,#f4f1ee 0%,#d9cfc4 35%,#4a3a36 60%,#c97a5a 100%)}
  .hero-right{left:393px;top:105px;width:345px;height:272px;background:linear-gradient(160deg,#eef0ea 0%,#b9c4b6 40%,#a05a6a 65%,#d8a07a 100%)}

  /* section headings */
  .section-bar{left:94px;width:644px;height:39px;background:var(--pink);font-size:22px;font-weight:400;line-height:38px;padding-left:7px}

  /* category tiles */
  .tile{background:var(--card);border:1px solid var(--card-edge);padding:6px}
  .tile .photo{position:relative;width:100%;height:100%}
  .tile .label{position:absolute;left:0;right:0;bottom:0;height:28px;background:var(--label-bg)}
  .tile .name{position:absolute;left:12px;bottom:2px;font-family:"Didact Gothic","Jost",sans-serif;font-size:24px;letter-spacing:1.5px;color:var(--white);text-transform:uppercase}
  .tile .view{position:absolute;right:0;bottom:0;width:53px;height:28px;background:var(--pink);font-family:"Jost",sans-serif;font-size:10.5px;line-height:10px;text-align:center;padding-top:4px}

  /* best sellers */
  .product{background:var(--card);border:1px solid var(--card-edge);padding:6px;width:157px;height:182px;top:790px}
  .product .photo{position:relative;width:100%;height:100%}
  .product .title{position:absolute;left:6px;top:123px;font-family:"Jost",sans-serif;font-size:12.5px;color:var(--white);white-space:nowrap}
  .product .buy{position:absolute;left:0;right:0;bottom:0;height:28px;background:var(--label-bg)}
  .product .price{position:absolute;left:12px;bottom:5px;font-family:"Jost",sans-serif;font-size:14px;color:var(--white)}
  .product .add{position:absolute;right:0;bottom:0;width:52px;height:28px;background:var(--pink);font-family:"Jost",sans-serif;font-size:10.5px;line-height:10px;text-align:center;padding-top:4px}

  /* footer */
  .site-footer{left:0;top:995px;width:832px;height:180px;background:var(--footer)}
  .foot-title{top:1003px;font-style:italic;font-size:15px;color:var(--pink-soft)}
  .sitemap{font-size:11px;line-height:20.5px}
  .subnav{font-size:9.5px;line-height:18.5px;color:var(--pink-soft)}
  .newsletter-copy{left:359px;top:1027px;width:160px;font-size:10.5px;line-height:13px}
  .field{left:359px;width:158px;height:21px;background:var(--field);border:1px solid var(--field-edge);font-size:8.5px;color:#aaaaaa;line-height:19px;padding-left:8px}
  .send{left:359px;top:1124px;width:158px;height:21px;background:var(--pink);font-size:10.5px;text-align:center;line-height:21px}
  .pay-card{width:41px;height:26px;border:1px solid #cccccc;border-radius:2px}
  .foot-brand{left:670px;top:1114px;width:68px;text-align:center;font-weight:300;font-size:15px;line-height:17px;color:var(--white)}
  .copyright{left:0;top:1175px;width:832px;height:25px;background:var(--pink);font-size:8.5px;text-align:center;line-height:25px}
</style>
</head>
<body>

<header class="abs site-header"></header>
<div class="abs utility cart">View Cart</div>
<div class="abs utility items">Items / $0.00</div>
<div class="abs brand">parlour nine hopes</div>
<nav class="abs main-nav">
  <a class="current">Home</a><a>About Us</a><a>Products</a><a>Catalogue</a><a>Contact Us</a>
</nav>
<div class="abs social" aria-label="Social links">
  <span><svg width="9" height="7" viewBox="0 0 9 7"><rect x=".5" y=".5" width="8" height="6" fill="none" stroke="#e8105e"/><path d="M.5 .5 4.5 4 8.5 .5" fill="none" stroke="#e8105e"/></svg></span>
  <span></span><span></span><span></span>
</div>

<section>
  <div class="abs hero-band"></div>
  <div class="abs hero-left" role="img" aria-label="Children's room with a jute rug ringed by coloured felt balls, a small white desk and chair"></div>
  <div class="abs hero-right" role="img" aria-label="Bedroom with a carved magenta headboard, patterned quilt and cushions beside a window"></div>
</section>

<h2 class="abs section-bar" style="top:378px">Products Categories</h2>

<div class="abs tile" style="left:94px;top:427px;width:208px;height:139px">
  <div class="photo" role="img" aria-label="Folded multicoloured pompom throws" style="background:linear-gradient(135deg,#b58a6a,#6e4a6a 40%,#c9a24a 70%,#8b3a4a)">
    <div class="label"></div><div class="name">Rugs</div><div class="view">View<br>Range</div>
  </div>
</div>
<div class="abs tile" style="left:312px;top:427px;width:208px;height:139px">
  <div class="photo" role="img" aria-label="White plate of green grapes on a wooden table" style="background:linear-gradient(160deg,#d9b48a,#c09a70 45%,#f0eee8 60%,#9ab04a 75%,#b08a60)">
    <div class="label"></div><div class="name">Dine</div><div class="view">View<br>Range</div>
  </div>
</div>
<div class="abs tile" style="left:530px;top:427px;width:208px;height:139px">
  <div class="photo" role="img" aria-label="Bathroom shelf with jars, starfish and towels" style="background:linear-gradient(150deg,#e8e2d8,#c8bca8 45%,#e0b060 65%,#d8d0c4)">
    <div class="label"></div><div class="name">Bathe</div><div class="view">View<br>Range</div>
  </div>
</div>
<div class="abs tile" style="left:94px;top:578px;width:208px;height:138px">
  <div class="photo" role="img" aria-label="Bed with a green quilt, patterned cushions and a brass lamp" style="background:linear-gradient(150deg,#eeeeee,#c8c8c8 35%,#4a8a7a 65%,#9a6a8a)">
    <div class="label"></div><div class="name">Sleep</div><div class="view">View<br>Range</div>
  </div>
</div>
<div class="abs tile" style="left:312px;top:578px;width:426px;height:138px">
  <div class="photo" role="img" aria-label="Bright felt ball rug beside felt garlands hanging by a white decorative head" style="background:linear-gradient(90deg,#e84a6a,#f0a030 20%,#4ab0a0 35%,#f2f0ee 50%,#e6e4e2 80%,#d8b0b8)">
    <div class="label"></div><div class="name">Decorative</div><div class="view">View<br>Range</div>
  </div>
</div>

<h2 class="abs section-bar" style="top:742px">Best Selling Items</h2>

<div class="abs product" style="left:94px">
  <div class="photo" role="img" aria-label="Jute rug with coloured felt ball border" style="background:linear-gradient(150deg,#e86a9a,#d8b890 40%,#c8a070 70%,#e8d040)">
    <div class="title">Lorem Ipsum proin gr</div><div class="buy"></div><div class="price">$50.95</div><div class="add">Add to<br>Cart</div>
  </div>
</div>
<div class="abs product" style="left:257px">
  <div class="photo" role="img" aria-label="Stack of patterned floor cushions" style="background:linear-gradient(180deg,#f2f0ee,#8a9a4a 25%,#c86a4a 50%,#6a8aa0 70%,#c0503a)">
    <div class="title">Lorem Ipsum proin gr</div><div class="buy"></div><div class="price">$50.95</div><div class="add">Add to<br>Cart</div>
  </div>
</div>
<div class="abs product" style="left:418px">
  <div class="photo" role="img" aria-label="Felt ball garland on a timber floor" style="background:linear-gradient(140deg,#c08a5a,#e04a7a 30%,#4ab0c0 55%,#e8c040 75%,#b07a4a)">
    <div class="title">Lorem Ipsum proin gr</div><div class="buy"></div><div class="price">$50.95</div><div class="add">Add to<br>Cart</div>
  </div>
</div>
<div class="abs product" style="left:581px">
  <div class="photo" role="img" aria-label="Pink and purple patterned cushions against a carved headboard" style="background:linear-gradient(150deg,#e8e8e8,#c0c0c0 30%,#c07aa0 60%,#8a5a8a)">
    <div class="title">Lorem Ipsum proin gr</div><div class="buy"></div><div class="price">$50.95</div><div class="add">Add to<br>Cart</div>
  </div>
</div>

<footer class="abs site-footer"></footer>
<div class="abs foot-title" style="left:94px">Site map</div>
<div class="abs sitemap" style="left:94px;top:1026px">Home<br>About Us<br>Catalogue<br>Contact Us</div>
<div class="abs sitemap" style="left:183px;top:1026px">Products</div>
<div class="abs subnav" style="left:192px;top:1048px">-- Rugs<br>-- Bathe<br>-- Dine<br>-- Decorative<br>-- Sleep</div>

<div class="abs foot-title" style="left:359px">Newsletter</div>
<p class="abs newsletter-copy">Sign up to be the first to receive the latest news, exclusive offers &amp; styling tips!</p>
<div class="abs field" style="top:1075px">Name</div>
<div class="abs field" style="top:1099px">Email</div>
<div class="abs send">SEND</div>

<div class="abs foot-title" style="left:618px;width:120px;text-align:right">Payment Options</div>
<div class="abs pay-card" style="left:652px;top:1036px;background:#f2f2f2" aria-label="Accepted card"></div>
<div class="abs pay-card" style="left:695px;top:1036px;background:#1e2a5a" aria-label="Accepted card"></div>
<div class="abs pay-card" style="left:652px;top:1068px;background:#f2f2f2" aria-label="Accepted card"></div>
<div class="abs pay-card" style="left:695px;top:1068px;background:#f2f2f2" aria-label="Accepted card"></div>
<div class="abs foot-brand">parlour<br>nine<br>hopes</div>

<div class="abs copyright">Copyright © 2014 Parlour Nine Hopes | All rights reserved.</div>

</body>
</html>
```